Package Design for Silicone Cartridge

We are Corvalen Crest. We are looking to receive an amazing design for our packaging for silicone. We are tired of the same old home store construction tube. We want something professional, attractive, bold, and eye catching.

The cartridge background will be WHITE
Use the following colors - BLACK or GREY, GOLD, WHITE

Use Sticker Design somewhere on the cartridge

The design should include the following-
(Corvalen Logo & Name) on the package.
100% RTV SILICONE SEALANT
Approved for Granite, Marble, Quartz, Quartzite, Porcelain, Metal, Glass, Wood, & More
Anti-Microbial Formula
Non-Paintable
Premium Adhesion
FDA & USDA Compliant
Excellent UV and Color Stability
Lifetime Flexibility
VOC Compliant

Net 10.3 Fl Oz.

Removable Extra Long Cartridge Tip

On reverse side please add the following information-
CAUTION:
KEEP OUT OF REACH OF CHILDREN. Avoid skin and eye contact. On contact, uncured sealant could cause irrita on to skin and eyes. In case of eye contact, flush eyes with warm water for 15 minutes, call a physician. For skin contact, remove sealant with a paper towel. If swallowed, do not induce vomiting, call a physician. Dumaflex RTV2 is manufactured for professional use only. Refer to Safety Data Sheet (SDS) for further informa on.
PLEASE REFER TO TECHNICAL DATA SHEET FOR COMPLETE INFORMATION ABOUT THE PRODUCT

UPDATE: Please include warning- Also - utilize wendrock parameters.
UPDATE2: Include one above 100% RTV SILICONE add the following text XXL 150 or XXL 250

Target Market(s)

Construction

Industry/Entity Type

Store

Requirements
Must have
• a GREAT DESIGN.
Should not have
• a bad design.

```html
<!DOCTYPE html>
<html lang="en">
<head>
<meta charset="utf-8">
<title>Corvalen 100% RTV Silicone Sealant – Cartridge Label</title>
<link href="https://fonts.googleapis.com/css2?family=Oswald:wght@400;500;600;700&family=Barlow:wght@300;400;600&family=Barlow+Condensed:wght@500;600;700&display=swap" rel="stylesheet">
<style>
  :root{
    --bg:#e8e9eb;
    --gold:#d7c27e;
    --black:#000;
    --white:#fff;
    --grey:#d3d4d6;
    --red:#d8232a;
    --ink:#222;
  }
  *{margin:0;padding:0;box-sizing:border-box}
  html,body{width:1200px;height:1112px;overflow:hidden;background:var(--bg)}
  .canvas{position:relative;width:1200px;height:1112px}
  .view-label{position:absolute;top:78px;font:400 24px/1 'Oswald',sans-serif;color:var(--black);letter-spacing:.3px}
  .panel{position:absolute;top:130px;width:365px;height:922px;background:var(--white);overflow:hidden}
  .panel--front{left:193px}
  .panel--back{left:645px}
  .top-strip{position:absolute;left:0;top:0;width:100%;height:10px;background:var(--grey)}
  .gold-band{position:absolute;left:0;width:100%;background:var(--gold)}
  .black-zone{position:absolute;left:0;top:612px;width:100%;height:290px;background:var(--black)}
  .base-band{position:absolute;left:0;top:902px;width:100%;height:20px;background:var(--gold)}

  /* shared title lines */
  .title{position:absolute;color:var(--black);font-family:'Oswald',sans-serif;text-transform:uppercase;white-space:nowrap;line-height:1;transform-origin:left top}
  .title .pct{color:var(--gold);font-weight:700}

  /* front */
  .award-tab{position:absolute;left:41px;top:10px;width:58px;height:69px;background:var(--grey);border-radius:0 0 29px 29px}
  .award-tab svg{position:absolute;left:15px;top:10px}
  .brand-mark{position:absolute;left:190px;top:48px;display:flex;align-items:center;gap:6px;color:var(--gold);font:700 30px/1 'Oswald',sans-serif}
  .brand-mark .dot{width:16px;height:16px;border-radius:50%;background:var(--gold)}
  .front-title-1{left:49px;top:108px;font-size:90px;font-weight:600;letter-spacing:-2px;transform:scaleX(.83)}
  .front-title-1 .rtv{font-size:60px;font-weight:500;letter-spacing:0;margin-left:4px}
  .front-title-2{left:49px;top:197px;font-size:84px;font-weight:500;letter-spacing:-1px;transform:scaleX(.9)}
  .front-title-3{left:49px;top:283px;font-size:84px;font-weight:500;letter-spacing:-1px;transform:scaleX(.93)}
  .rule{position:absolute;left:47px;width:262px;height:3px;background:var(--gold)}
  .approved{position:absolute;left:0;top:395px;width:100%;text-align:center;font:400 16px/1.3 'Oswald',sans-serif;color:var(--black)}
  .photo-ring{position:absolute;left:42px;top:446px;width:280px;height:280px;border-radius:50%;background:var(--gold);padding:7px}
  .photo{width:100%;height:100%;border-radius:50%;background:radial-gradient(circle at 60% 40%,#f3efe9 0%,#e2dbd2 45%,#8f8a86 75%,#4a4747 100%)}
  .features{position:absolute;left:0;top:736px;width:366px;list-style:none;text-align:center;color:var(--white);font:300 17px/21px 'Barlow',sans-serif}
  .features li{display:block}
  .features svg{display:inline-block;vertical-align:-1px;margin-right:4px}
  .net-tab{position:absolute;left:282px;top:834px;width:59px;height:68px;background:var(--gold);border-radius:29px 29px 0 0;text-align:center;color:var(--white);font-family:'Oswald',sans-serif;font-weight:700}
  .net-tab .qty{display:block;padding-top:10px;font-size:27px;line-height:1;letter-spacing:-1px}
  .net-tab .unit{display:block;font-size:17px;line-height:1.2;font-weight:500}

  /* back */
  .back-title-1{left:41px;top:34px;font-size:52px;font-weight:600;letter-spacing:-1px;transform:scaleX(.84)}
  .back-title-1 .rtv{font-size:32px;font-weight:500;letter-spacing:0;margin-left:3px}
  .back-title-2{left:41px;top:82px;font-size:52px;font-weight:500;letter-spacing:-.5px;transform:scaleX(.82)}
  .back-title-3{left:41px;top:130px;font-size:52px;font-weight:500;letter-spacing:-.5px;transform:scaleX(.86)}
  .seal{position:absolute;left:207px;top:62px;width:106px;height:106px;border-radius:50%;background:var(--black);border:4px solid #555}
  .seal::after{content:"";position:absolute;inset:18px;border-radius:50%;background:var(--gold)}
  .hazard{position:absolute;left:50px;top:196px}
  .warning{position:absolute;left:127px;top:196px;width:195px;font:300 11.2px/14.8px 'Barlow',sans-serif;color:var(--ink);text-align:justify}
  .warning h3{font:600 12.5px/14px 'Barlow Condensed',sans-serif;color:var(--black);letter-spacing:.3px}
  .safety{position:absolute;left:42px;top:272px;width:280px;font:300 11.2px/14.8px 'Barlow',sans-serif;color:var(--ink);text-align:justify}
  .safety b{font-family:'Barlow Condensed',sans-serif;font-weight:700;color:var(--black);letter-spacing:.3px}
  .band-title{position:absolute;left:42px;top:573px;white-space:nowrap;font:600 29px/1 'Oswald',sans-serif;color:var(--white);letter-spacing:-.3px;transform:scaleX(.83);transform-origin:left top}
  .caution{position:absolute;left:42px;top:628px;width:281px;font:300 11.2px/14.8px 'Barlow',sans-serif;color:var(--white);text-align:justify}
  .caution .lead{color:var(--gold);font:600 11.6px/14.8px 'Barlow Condensed',sans-serif;text-transform:uppercase;letter-spacing:.2px;text-align:justify}
  .icon-box{position:absolute;left:42px;top:826px;width:281px;height:56px;border:2px solid var(--white);display:flex;align-items:center;justify-content:center;color:var(--white);font:600 12px/1 'Barlow Condensed',sans-serif;letter-spacing:.3px}
</style>
</head>
<body>
<div class="canvas">
  <h2 class="view-label" style="left:194px">FRONT VIEW</h2>
  <h2 class="view-label" style="left:646px">BACK VIEW</h2>

  <!-- Front -->
  <section class="panel panel--front">
    <div class="top-strip"></div>
    <div class="award-tab">
      <svg width="28" height="40" viewBox="0 0 28 40" aria-hidden="true">
        <circle cx="14" cy="14" r="12" fill="none" stroke="#fff" stroke-width="2.5"/>
        <circle cx="14" cy="14" r="6" fill="#fff"/>
        <path d="M7 24 L3 38 L9 34 L12 39 L14 27 M21 24 L25 38 L19 34 L16 39 L14 27" fill="#fff"/>
      </svg>
    </div>
    <div class="brand-mark"><span class="dot"></span>Corvalen</div>

    <div class="title front-title-1"><span class="pct">100%</span><span class="rtv">RTV</span></div>
    <div class="title front-title-2">SILICONE</div>
    <div class="title front-title-3">SEALANT</div>
    <div class="rule" style="top:380px"></div>
    <div class="rule" style="top:387px"></div>
    <p class="approved">Approved for Granite, Marble, Quartz, Quartzite,<br>Porcelain, Metal, Glass, Wood, &amp; More</p>

    <div class="gold-band" style="top:562px;height:50px"></div>
    <div class="black-zone"></div>
    <div class="photo-ring"><div class="photo" role="img" aria-label="Photo of a hand applying silicone sealant along a tiled edge"></div></div>

    <ul class="features">
      <li><svg width="16" height="13" viewBox="0 0 16 13" aria-hidden="true"><path d="M1 7 L6 12 L15 2" fill="none" stroke="var(--gold)" stroke-width="3"/></svg>Anti-Microbial Formula</li>
      <li><svg width="16" height="13" viewBox="0 0 16 13" aria-hidden="true"><path d="M1 7 L6 12 L15 2" fill="none" stroke="var(--gold)" stroke-width="3"/></svg>Excellent UV and Color Stability</li>
      <li><svg width="16" height="13" viewBox="0 0 16 13" aria-hidden="true"><path d="M1 7 L6 12 L15 2" fill="none" stroke="var(--gold)" stroke-width="3"/></svg>FDA &amp; USDA Compliant</li>
      <li><svg width="16" height="13" viewBox="0 0 16 13" aria-hidden="true"><path d="M1 7 L6 12 L15 2" fill="none" stroke="var(--gold)" stroke-width="3"/></svg>Premium Adhesion</li>
      <li><svg width="16" height="13" viewBox="0 0 16 13" aria-hidden="true"><path d="M1 7 L6 12 L15 2" fill="none" stroke="var(--gold)" stroke-width="3"/></svg>Lifetime Flexibility</li>
      <li><svg width="16" height="13" viewBox="0 0 16 13" aria-hidden="true"><path d="M1 7 L6 12 L15 2" fill="none" stroke="var(--gold)" stroke-width="3"/></svg>VOC Compliant</li>
      <li><svg width="16" height="13" viewBox="0 0 16 13" aria-hidden="true"><path d="M1 7 L6 12 L15 2" fill="none" stroke="var(--gold)" stroke-width="3"/></svg>Non-Paintable</li>
    </ul>
    <div class="net-tab"><span class="qty">10.3</span><span class="unit">FL OZ</span></div>
    <div class="base-band"></div>
  </section>

  <!-- Back -->
  <section class="panel panel--back">
    <div class="top-strip"></div>
    <div class="title back-title-1"><span class="pct">100%</span><span class="rtv">RTV</span></div>
    <div class="title back-title-2">SILICONE</div>
    <div class="title back-title-3">SEALANT</div>
    <div class="seal" aria-hidden="true"></div>

    <svg class="hazard" width="70" height="70" viewBox="0 0 70 70" aria-hidden="true">
      <rect x="14" y="14" width="42" height="42" transform="rotate(45 35 35)" fill="#fff" stroke="var(--red)" stroke-width="4"/>
      <path d="M32 19 H38 L37 41 H33 Z" fill="#000"/>
      <circle cx="35" cy="48" r="3.6" fill="#000"/>
    </svg>
    <div class="warning">
      <h3>WARNING</h3>
      Causes serious eye irritation. May cause an allergic skin reaction. Harmful to aquatic life with long lasting effects. Read label before use.
    </div>
    <p class="safety"><b>KEEP OUT OF REACH OF CHILDREN.</b> If medical advice is needed, have product container or label at hand. Obtain special instructions before use. Do not handle until all safety precautions have been read and understood. Use personal protective equipment as required. Wear protective gloves. Wear eye or face protection. Avoid release to the environment. Avoid breathing dust. Wash hands thoroughly after handling. Contaminated work clothing should not be allowed out of the workplace. If exposed or concerned: Get medical attention.<br><b>IF ON SKIN:</b> Wash with plenty of soap and water. Wash contaminated clothing before reuse. If skin irritation or rash occurs: Get medical attention.<br><b>IF IN EYES:</b> Rinse cautiously with water for several minutes. Remove contact lenses, if present and easy to do. Continue rinsing. If eye irritation persists: Get medical attention. Store locked up. Dispose of contents and container in accordance with all local, regional, national and international regulations.</p>

    <div class="gold-band" style="top:562px;height:50px"></div>
    <div class="band-title">100% RTV SILICONE SEALANT</div>
    <div class="black-zone"></div>
    <div class="caution">
      <p class="lead">CAUTION:<br>Direct contact of uncured sealant irritates eyes and may irritate skin. Overexposure to vapor may irritate eyes, nose and throat.</p>
      <p>Avoid eye and skin contact. Use only outdoors or in a well-ventilated area. Do not handle contact lenses with sealant on hands. IN CASE OF EYE CONTACT, flush eyes with water for 15 minutes. Obtain medical attention. IN CASE OF SKIN CONTACT, remove from skin and flush with water. Sealant releases acetic acid (vinegar-like odor) during cure. KEEP OUT OF REACH OF CHILDREN. FOR INDUSTRIAL USE ONLY.</p>
    </div>
    <div class="icon-box">OTHER ICONS +BARCODE</div>
    <div class="base-band"></div>
  </section>
</div>
</body>
</html>
```